Kestrel Orchard Fliers and logo design

We need to design a product logo and some informational fliers for a pebble quest.
I have attached our Kestrel Orchard logo - colours need to be complimentary but not the same, we would like fresh, funky but still professional. We generally communicate in a fairly casual way to reach our market. (We don't like boring)
Clear and simple - not too busy
images are good but not actual photos
Here is our website to give you an idea www.kestrelorchard.co.nz
The flier is a 3 page document.
The logo is to say Pebble Quest. The challenge is based on exercise, connecting with people, giving, learning and taking notice (The 7 stones of Marlow) Once agin the logo needs to be complementary but not the same.
The Kestrel orchard logo needs to be on the fliers but the pebble quest logo is separate.
Thanks very much!!

```html
<!DOCTYPE html>
<html lang="en">
<head>
<meta charset="utf-8">
<title>Kestrel Orchard fliers</title>
<link href="https://fonts.googleapis.com/css2?family=Montserrat:wght@600;700;800&family=Source+Sans+3:wght@400;600;700&display=swap" rel="stylesheet">
<style>
:root{
  --orange:#d9593a;
  --teal:#5cc4a6;
  --ink:#333333;
  --stage:#c9c9c9;
  --paper:#f4f4f4;
  --panel:#e2e2e2;
}
*{box-sizing:border-box;margin:0;padding:0}
html,body{width:1200px;height:1200px;overflow:hidden;background:var(--stage)}
body{position:relative;font-family:"Source Sans 3",Arial,sans-serif;color:var(--ink)}
.sheet{position:absolute;background:linear-gradient(#fff,var(--paper));box-shadow:0 2px 6px rgba(0,0,0,.25);overflow:hidden}
.sheet--stop{left:414px;top:53px;width:414px;height:536px}
.sheet--values{left:173px;top:610px;width:411px;height:532px}
.sheet--tips{left:618px;top:610px;width:417px;height:537px}
.brand{position:absolute;display:flex;align-items:flex-start;gap:6px}
.brand__dot{width:14px;height:14px;border-radius:50%;background:var(--orange);margin-top:4px}
.brand__name{font-family:"Source Sans 3",Arial,sans-serif;font-weight:700;color:var(--teal);font-size:25px;line-height:22px;letter-spacing:-.3px}
.pill{position:absolute;height:26px;border-radius:13px;background:var(--orange);color:#fff;font-family:"Montserrat",Arial,sans-serif;font-weight:700;font-size:12px;display:flex;align-items:center;justify-content:center}
.photo{position:absolute}
/* page one */
.stop-head{position:absolute;left:0;right:0;top:116px;text-align:center;font-family:"Montserrat",Arial,sans-serif}
.stop-head__lead{color:var(--orange);font-size:11.5px;font-weight:600}
.stop-head__main{color:var(--teal);font-size:14px;font-weight:800;margin-top:4px}
.steps{position:absolute;left:17px;top:161px;width:202px}
.step__tag{display:inline-block;height:20px;line-height:20px;width:97px;padding-left:6px;background:var(--orange);color:#fff;font-family:"Montserrat",Arial,sans-serif;font-weight:700;font-size:11.5px;clip-path:polygon(0 0,100% 0,88% 100%,0 100%)}
.step__text{font-size:6.2px;line-height:8px;margin:5px 0 6px}
.step__text b{font-weight:700}
.stop-copy{position:absolute;left:226px;top:160px;width:171px;font-size:7.8px;line-height:10px;text-align:justify}
.stop-copy p{margin-bottom:9px}
/* page two */
.banner{position:absolute;background:var(--teal);color:#fff}
.banner--values{left:190px;top:27px;right:0;height:49px;padding:6px 10px}
.banner__title{font-family:"Montserrat",Arial,sans-serif;font-weight:800;font-size:16px}
.banner__sub{font-size:6.2px;line-height:7.6px;margin-top:2px}
.vstep{position:absolute;left:15px;width:380px}
.vstep__title{color:var(--orange);font-family:"Montserrat",Arial,sans-serif;font-weight:700;font-size:8px}
.vstep__text{font-size:6.2px;line-height:7.8px}
.value-table{position:absolute;left:15px;top:134px;width:380px;height:236px;background:var(--panel);clip-path:polygon(0 0,94% 0,100% 6%,100% 100%,0 100%)}
.value-col{position:absolute;top:10px;list-style:none;font-size:6.2px;line-height:8.05px;font-weight:600}
.value-rule{position:absolute;top:10px;width:1px;height:216px;background:#777}
.blank{position:absolute;display:flex;align-items:flex-end;width:178px;font-family:"Montserrat",Arial,sans-serif;font-weight:700;color:var(--orange);font-size:8.5px}
.blank span{flex:1;border-bottom:1px solid #555;margin-left:6px;height:6px}
/* page three */
.banner--tips{left:194px;top:27px;right:0;height:50px;padding:8px 11px;font-family:"Montserrat",Arial,sans-serif;font-weight:800;font-size:13.5px;line-height:17px}
.promise{position:absolute;left:0;right:0;top:102px;height:64px;background:var(--orange);color:#fff;font-size:12px;line-height:15px;padding:9px 16px}
.tips-lead{position:absolute;left:16px;top:177px;font-weight:700;font-size:7.3px}
.tips{position:absolute;left:16px;top:193px;width:386px;list-style:none;font-size:6.6px;line-height:8.3px}
.tips li{margin-bottom:5px}
.tips b{font-weight:700}
</style>
</head>
<body>

<section class="sheet sheet--stop">
  <div class="brand" style="left:17px;top:40px"><span class="brand__name">kestrel<br>orchard</span><span class="brand__dot"></span></div>
  <svg class="photo" style="left:290px;top:0" width="124" height="110" viewBox="0 0 124 110">
    <path d="M0 0 H70 A46 46 0 0 1 24 46 A24 24 0 0 1 0 22 Z" fill="var(--orange)"/>
    <circle cx="88" cy="83" r="24" fill="var(--teal)"/>
    <defs><linearGradient id="hike" x1="0" y1="0" x2="0" y2="1"><stop offset="0" stop-color="#c9d6de"/><stop offset=".5" stop-color="#8a8a7a"/><stop offset="1" stop-color="#5d5a4a"/></linearGradient></defs>
    <circle cx="68" cy="40" r="46" fill="url(#hike)" role="img" aria-label="Hiker walking across a rocky mountain ridge"/>
  </svg>
  <div class="stop-head">
    <div class="stop-head__lead">We cannot control what happens to us in life,</div>
    <div class="stop-head__main">BUT WE CAN CHANGE THE WAY WE REACT</div>
  </div>
  <div class="steps">
    <div class="step__tag">S = Stop</div>
    <p class="step__text">Stop what you are doing: Press the pause button on your thoughts and actions.</p>
    <div class="step__tag">T = Take</div>
    <p class="step__text">Take a few deep breaths to centre yourself and bring yourself fully into the present moment.</p>
    <div class="step__tag">O = Observe</div>
    <p class="step__text">Observe what is going on with your:<br><b>1.Body</b><br>What physical sensations are you aware of (touch, sight, hearing, taste, smell)?<br><b>Emotions</b><br>What are you feeling right now?<br><b>2.Mind</b><br>What assumptions are your making about your feelings? What is the story you're telling yourself about why you are having them?</p>
    <div class="step__tag">P = Proceed</div>
    <p class="step__text">Proceed with whatever you were doing, making a conscious, intentional choice to incorporate what you just learned.</p>
  </div>
  <div class="stop-copy">
    <p>Stress happens because we are allowing fear, anger, disappointment and a host of other negative emotions to navigate our actions. By becoming aware of these emotions and allowing them to simply be, we can begin to gain control of how we react and respond to stressful situations.</p>
    <p>Our experience is always changing. Without awareness, mental patterns related to what we fear and what upsets us make life harder.</p>
    <p>S.T.O.P is a powerful, yet surprisingly basic strategy that helps you to be focused, alert, relaxed and at your emotional best when stressful moments present themselves in your life.</p>
    <p>Simply put, it's a four-step checklist to use anytime you want to ground yourself and get some insight into whatever is going on. The whole idea behind it is that by taking a very brief break—even less than one minute—you can determine the very best action to take in the moment.</p>
  </div>
  <div class="photo" style="left:0;right:0;top:390px;bottom:0;background:linear-gradient(180deg,rgba(244,244,244,1) 0%,rgba(214,170,150,.7) 35%,#8c6a66 70%,#3d4a6a 100%)" role="img" aria-label="Speaker facing a large blurred audience"></div>
  <div class="pill" style="left:110px;top:493px;width:212px">kestrelorchard.co.nz</div>
</section>

<section class="sheet sheet--values">
  <div class="brand" style="left:15px;top:24px"><span class="brand__name">kestrel<br>orchard</span><span class="brand__dot"></span></div>
  <div class="banner banner--values">
    <div class="banner__title">Values</div>
    <div class="banner__sub">This exercise is designed to help you reach a better understanding of your most significant values.</div>
  </div>
  <div class="vstep" style="top:100px">
    <div class="vstep__title">Step 1: What I Value Most...</div>
    <p class="vstep__text">From this list of values (both work and personal), select the ten that are most important to you - as guides for how to behave, or as components of a valued way of life. Feel free to add any values of your own to this list.</p>
  </div>
  <div class="value-table">
    <ul class="value-col" style="left:27px"><li>Achievement</li><li>Advancement and promotion</li><li>Adventure</li><li>Affection (love and caring)</li><li>Arts</li><li>Challenging problems</li><li>Change and variety</li><li>Close relationships</li><li>Community</li><li>Competence</li><li>Competition</li><li>Cooperation</li><li>Country</li><li>Creativity</li><li>Decisiveness</li><li>Democracy</li><li>Ecological awareness</li><li>Economic security</li><li>Effectiveness</li><li>Efficiency</li><li>Ethical practice</li><li>Excellence</li><li>Excitement</li><li>Fame</li><li>Fast living</li><li>Financial gain</li><li>Freedom</li></ul>
    <div class="value-rule" style="left:130px"></div>
    <ul class="value-col" style="left:146px"><li>Friendships</li><li>Growth</li><li>Having a family</li><li>Helping other people</li><li>Helping society</li><li>Honesty</li><li>Independence</li><li>Influencing others</li><li>Inner harmony</li><li>Integrity</li><li>Intellectual status</li><li>Involvement</li><li>Job tranquility</li><li>Knowledge</li><li>Leadership</li><li>Location</li><li>Loyalty</li><li>Market position</li><li>Meaningful work</li><li>Merit</li><li>Money</li><li>Nature</li><li>Being around people who</li><li>are open and honest</li><li>Order (tranquility,</li><li>stability, conformity)</li><li>Personal development</li></ul>
    <div class="value-rule" style="left:238px"></div>
    <ul class="value-col" style="left:254px"><li>Physical challenge</li><li>Pleasure</li><li>Power and authority</li><li>Privacy</li><li>Public service</li><li>Purity</li><li>Quality of what I take part in</li><li>Quality relationships</li><li>Recognition (respect from others, status)</li><li>Religion</li><li>Reputation</li><li>Responsibility and accountability</li><li>Security</li><li>Self-Respect</li><li>Serenity</li><li>Sophistication</li><li>Stability</li><li>Status</li><li>Supervising others</li><li>Time freedom</li><li>Truth</li><li>Wealth</li><li>Wisdom</li><li>Work under pressure</li><li>Work with others</li><li>Working alone</li></ul>
  </div>
  <div class="vstep" style="top:379px">
    <div class="vstep__title">Step 2: Elimination</div>
    <p class="vstep__text">Now that you have identified ten, imagine that you are only permitted to have five values. Which five would you give up? Cross them off. Put them into order, the one that is most important to you first. Write it somewhere and refer to it when you can't make a decision, align yourself with what makes you feel good.</p>
  </div>
  <div class="blank" style="left:15px;top:418px">1<span></span></div>
  <div class="blank" style="left:213px;top:418px">3<span></span></div>
  <div class="blank" style="left:15px;top:445px">2<span></span></div>
  <div class="blank" style="left:213px;top:445px">4<span></span></div>
  <div class="vstep" style="top:466px">
    <div class="vstep__title">Step 3: Support yourself</div>
    <p class="vstep__text">Write it somewhere and refer to it when you can't make a decision, align yourself with what makes you feel good.</p>
  </div>
  <div class="pill" style="left:106px;top:494px;width:211px">kestrelorchard.co.nz</div>
</section>

<section class="sheet sheet--tips">
  <div class="brand" style="left:16px;top:24px"><span class="brand__name">kestrel<br>orchard</span><span class="brand__dot"></span></div>
  <div class="banner banner--tips">10 TIPS TO IMPROVE YOUR<br>WELLBEING</div>
  <p class="promise">Yes, you will have to get off the couch and you might need to say no to burgers for lunch every day but we promise we won't turn you into spandex wearing vegans with prescriptions to Glowbox!</p>
  <p class="tips-lead">Small changes every day can make a huge difference.</p>
  <ol class="tips">
    <li><b>1. Put on your wake up grin</b> - Smile and think happy thoughts – that first 90 secs has a big impact on your day. If you start the day with bad thoughts, then it compounds – simply turn up the corners of your mouth you'll start to release endorphins and serotonin, your feel-good hormones.</li>
    <li><b>2. Drink lemon and warm water first thing</b> – and keep drinking water all day. It will cleanse your liver, you will eat less, you'll feel better and have a clearer head.</li>
    <li><b>3. Exercise</b> – it boosts the happy chemicals in your brain. So Be Active - get your heart rate going and stretch those muscles. At the very least take the stairs. To get your endorphins surging you'll need to really heavy breathe – so walk up those stairs faster, do your house work quicker – get that heart pumping.</li>
    <li><b>4. Eat a banana</b> – Did you ever see a depressed chimp? Bananas help to lessen feelings of stress and anxiety due to high levels of tryptophan which converts to serotonin – one of those happy hormone. The high level of potassium helps you to be more alert and will give you energy.</li>
    <li><b>5. Put on your WOW! Glasses</b> – Go outside and Take Notice – The wind, the warmth, the cold, the trees, the blossom, the amazing sky, the moon. The world is full of things that make you go WOW, if you just slow down and Take Notice. Even better, go with a friend and Connect as well.</li>
    <li><b>6. 5 fruit and veg per day</b> – Get the fibre into to you… Without it you clog up, if you clog up you get grumpy and sluggish, if you get grumpy and sluggish – let's not go there! If you have trouble fitting the veges in, put them into a smoothie.</li>
    <li><b>7. Play music</b> – it cheers you up. Create a playlist for when you need a pick-me-up. Play it in the car to and from work, doing your housework or when you're going for that brisk walk, getting out of breath and send even more happy hormones to your brain. (No, not the sad break-up playlist!)</li>
    <li><b>8. Remove a poison</b> – Take away something that you know is bad for you – fast food, sugar, gluten – even for a couple of days a week – replace it with something healthy like water, fruit, veg, quinoa, exercise whatever works for you.</li>
    <li><b>9. Kill em with kindness</b> – When you're feeling bad, do something nice for someone else and it will make their day and you'll feel even better. In fact, Give every day.</li>
    <li><b>10. Keep the cogs turning</b> – Use it or lose it as they say – use your brain. Keep learning – something new every day.</li>
  </ol>
  <div class="photo" style="left:0;right:0;top:438px;bottom:0;background:linear-gradient(180deg,rgba(244,244,244,1) 0%,#c7d3dc 35%,#7d93a6 70%,#4f6275 100%)" role="img" aria-label="Person with arms outstretched above the clouds on a mountain top"></div>
  <div class="pill" style="left:98px;top:496px;width:214px">kestrelorchard.co.nz</div>
</section>

</body>
</html>
```